Company or website name
- Quellmor, LLC
- Quellmor, LLC
- Quellmor, LLC is a research, science and technology based manufacturing company that formulates, develops, manufactures and packages a full complement of personal care products for domestic and international concerns. We private label and contract package personal care products, cosmetics, bath salts and powders and home fragrance products. Quellmor is conveniently located in Southern California adjacent to major transportation hubs and international airports. We utilize earth friendly, green manufacturing processes, maximize the use of renewable resource raw materials and minimize the use of non-renewable and petrochemical based raw materials. We provide formulation and product development services with low minimum order quantities and short lead times. Quellmor is the intersection between nature, science, beauty and innovation. We are a B-2-B company.
- We're looking for an ad design that can be used for both banner and column use online and in print. We manufacture bath and body products such as bath salts, body washes, body powders, bath oils and bubble baths, hair care products such as shampoos, conditioners and styling aids, skin care products such as anti-aging creams, cleansers, masks, toners and serums, color cosmetics such as eyeliners, mascaras, foundations and mineral make-up powders, manicure/pedicure products such as cuticle oils, sugar and salt scrubs and foot soaks/softeners and spa products such as seaweed wraps, cellulite creams, body masks, massage oils and candles. Our strengths are natural and organic product formulation, low minimums, competitive prices, complete research &development services new and innovative ingredients and fast turnaround times. Examples can be found at the following sites: http://www.zuvvo.com/ http://www.grovemantleboard.org/ http://www.trellisfinchjournal.com/ http://pondrixa.org/images/downloads/lumaletters/2009-10-lumaletter.pdf http://www.brindlewoxpress.com/

```html
<!DOCTYPE html>
<html lang="en">
<head>
<meta charset="utf-8">
<title>Quellmor, LLC – Product Ads</title>
<link rel="stylesheet" href="https://fonts.googleapis.com/css2?family=Tinos:wght@400;700&display=swap">
<style>
  :root{
    --page-bg:#000;
    --panel-bg:#fff;
    --ink:#222;
    --hair:#cf2438;
    --skin:#a37318;
    --baby:#5a8a1d;
    --bath:#36b8cc;
    --logo-ink:#b3412c;
  }
  *{box-sizing:border-box;margin:0;padding:0}
  html,body{width:1200px;height:425px;overflow:hidden;background:var(--page-bg)}
  body{font-family:"Tinos","Times New Roman",serif;color:var(--ink)}
  .ad-row{position:relative;width:1200px;height:425px;display:flex;gap:9px;padding:13px 14px 16px}
  .ad{position:relative;width:286px;height:396px;background:var(--panel-bg);overflow:hidden}
  .ad--hair{--accent:var(--hair)}
  .ad--skin{--accent:var(--skin)}
  .ad--baby{--accent:var(--baby)}
  .ad--bath{--accent:var(--bath)}
  .hero{position:absolute;left:0;top:0;width:100%;height:175px}
  .hero--hair{background:linear-gradient(110deg,#0d0d0d 0%,#3a3a3c 45%,#c9a38e 70%,#f2f2f2 100%)}
  .hero--skin{background:linear-gradient(180deg,#5cc6e2 0%,#9fdbe8 40%,#c99778 62%,#b8826a 100%)}
  .hero--baby{background:linear-gradient(160deg,#e9f3f7 0%,#c9dde6 40%,#f0d6c6 65%,#ffffff 100%)}
  .hero--bath{background:linear-gradient(200deg,#1e9ec9 0%,#4fc0dc 40%,#d9b29c 70%,#3aa9cf 100%)}
  .brand{position:absolute;top:8px;left:6px;display:flex;align-items:center;gap:4px;background:#fff;border-radius:12px;padding:3px 8px 3px 5px;height:26px}
  .brand--right{left:auto;right:6px}
  .brand__dot{width:11px;height:11px;border-radius:50%;background:var(--logo-ink)}
  .brand__name{font-size:15px;font-weight:700;color:var(--logo-ink)}
  .headline{position:absolute;top:181px;left:0;width:100%;text-align:center;font-size:17.5px;line-height:22px;color:var(--accent)}
  .features{position:absolute;top:236px;left:0;width:100%;text-align:center;font-size:7.6px;line-height:12px;letter-spacing:.1px;text-transform:uppercase}
  .divider{position:absolute;top:268px;left:70px;width:146px;height:6px}
  .category{position:absolute;top:281px;left:50%;transform:translateX(-50%);background:var(--accent);color:#fff;font-size:8.6px;font-weight:700;padding:2px 8px;white-space:nowrap;letter-spacing:.3px}
  .category--side{left:34px;transform:none;top:286px;text-align:left;line-height:10px;padding:2px 6px}
  .products{position:absolute;top:296px;left:50%;transform:translateX(-50%);width:96px;height:52px;border-radius:4px}
  .products--hair{background:linear-gradient(90deg,#f4c23a,#e8a4b9,#ffffff,#f08a3a)}
  .products--skin{background:linear-gradient(90deg,#e9e4d6,#f7f3ea,#c8d4d8,#e3d2b0)}
  .products--baby{left:132px;transform:none;top:292px;width:124px;height:60px;background:linear-gradient(90deg,#e96aa5,#7fbde8,#f2f2f2,#bfe3f2)}
  .products--bath{width:240px;background:linear-gradient(90deg,#f2b24a,#eef0f2,#9aa6b2,#e8b07a,#a9cf7a)}
  .range{position:absolute;top:351px;left:0;width:100%;text-align:center;font-size:7.6px;text-transform:uppercase;white-space:nowrap}
  .range--bold{font-weight:700;font-size:8.4px;top:348px}
  .footer{position:absolute;left:0;bottom:0;width:100%;height:32px;background:var(--accent);color:#fff;text-align:center;font-size:8.3px;line-height:12px;padding-top:4px}
</style>
</head>
<body>
<main class="ad-row">

  <article class="ad ad--hair">
    <div class="hero hero--hair" role="img" aria-label="Woman with long glossy dark hair in profile"></div>
    <div class="brand"><span class="brand__dot"></span><span class="brand__name">Quellmor</span></div>
    <h2 class="headline">Creating Innovative Products<br>by Blending Science and Nature</h2>
    <p class="features">FDA Registered &nbsp;I&nbsp; Fast Turnaround &nbsp;I&nbsp; Low Minimums<br>Competitive Pricing &nbsp;I&nbsp; CGMP Quality Control</p>
    <svg class="divider" viewBox="0 0 146 6"><line x1="0" y1="3" x2="146" y2="3" stroke="#555" stroke-width=".8"/></svg>
    <span class="category">HAIR CARE PRODUCTS</span>
    <div class="products products--hair" role="img" aria-label="Assorted shampoo and conditioner bottles"></div>
    <p class="range">Shampoos &nbsp;I&nbsp; Conditioners &nbsp;I&nbsp; Pomades and Styling Products</p>
    <footer class="footer">1280 W. Larkfield Avenue Building 40, Corvella, CA 90210<br>555.010.2481 P 555.010.2482 F info@quellmor.com</footer>
  </article>

  <article class="ad ad--skin">
    <div class="hero hero--skin" role="img" aria-label="Woman applying lotion to her shoulder at the beach"></div>
    <div class="brand"><span class="brand__dot"></span><span class="brand__name">Quellmor</span></div>
    <h2 class="headline">Creating Innovative Products<br>by Blending Science and Nature</h2>
    <p class="features">FDA Registered &nbsp;I&nbsp; Fast Turnaround &nbsp;I&nbsp; Low Minimums<br>Competitive Pricing &nbsp;I&nbsp; CGMP Quality Control</p>
    <svg class="divider" viewBox="0 0 146 6"><line x1="0" y1="3" x2="146" y2="3" stroke="#555" stroke-width=".8"/></svg>
    <span class="category">SKIN CARE PRODUCTS</span>
    <div class="products products--skin" role="img" aria-label="Skin care jars, tubes and serum bottles"></div>
    <p class="range">Shampoos &nbsp;I&nbsp; Conditioners &nbsp;I&nbsp; Pomades and Styling Products</p>
    <footer class="footer">1280 W. Larkfield Avenue Building 40, Corvella, CA 90210<br>555.010.2481 P 555.010.2482 F info@quellmor.com</footer>
  </article>

  <article class="ad ad--baby">
    <div class="hero hero--baby" role="img" aria-label="Smiling toddler in a foamy bath"></div>
    <div class="brand"><span class="brand__dot"></span><span class="brand__name">Quellmor</span></div>
    <h2 class="headline">Creating Innovative Products<br>by Blending Science and Nature</h2>
    <p class="features">FDA Registered &nbsp;I&nbsp; Fast Turnaround &nbsp;I&nbsp; Low Minimums<br>Competitive Pricing &nbsp;I&nbsp; CGMP Quality Control</p>
    <svg class="divider" viewBox="0 0 146 6"><line x1="0" y1="3" x2="146" y2="3" stroke="#555" stroke-width=".8"/></svg>
    <span class="category category--side">BABY CARE<br>PRODUCTS</span>
    <div class="products products--baby" role="img" aria-label="Baby shampoo bottles, powder and folded towels"></div>
    <p class="range range--bold">Shampoos &nbsp;I&nbsp; Bubble Bath &nbsp;I&nbsp; Lotions and Baby Powders</p>
    <footer class="footer">1280 W. Larkfield Avenue Building 40, Corvella, CA 90210<br>555.010.2481 P 555.010.2482 F info@quellmor.com</footer>
  </article>

  <article class="ad ad--bath">
    <div class="hero hero--bath" role="img" aria-label="Woman relaxing in a blue pool"></div>
    <div class="brand brand--right"><span class="brand__dot"></span><span class="brand__name">Quellmor</span></div>
    <h2 class="headline">Creating Innovative Products<br>by Blending Science and Nature</h2>
    <p class="features">FDA Registered &nbsp;I&nbsp; Fast Turnaround &nbsp;I&nbsp; Low Minimums<br>Competitive Pricing &nbsp;I&nbsp; CGMP Quality Control</p>
    <svg class="divider" viewBox="0 0 146 6"><line x1="0" y1="3" x2="146" y2="3" stroke="#555" stroke-width=".8"/></svg>
    <span class="category">BATH PRODUCTS</span>
    <div class="products products--bath" role="img" aria-label="Bath gel tube, bath salts, body powder, lotion and bath oil bottles"></div>
    <p class="range">Bath Gels &nbsp;I&nbsp; Bath Salts &nbsp;I&nbsp; Body Powders &nbsp;I&nbsp; Lotions &nbsp;I&nbsp; Bath Oils</p>
    <footer class="footer">1280 W. Larkfield Avenue Building 40, Corvella, CA 90210<br>555.010.2481 P 555.010.2482 F info@quellmor.com</footer>
  </article>

</main>
</body>
</html>
```